We sell companies excess stock for them

We need a business card for a company based in New Zealand called 'StockHarbor'.

Check out our website to get an idea www.stockharbor.example

We help other businesses to;
- Sell Excess Stock
- Manage Product Returns
- Sell Company Assets

Our logo is attached for your reference
The font used is 'RifficFree-Bold'

Target Market(s)

Businesses

Industry/Entity Type

Business

Contact Information for Business Card

Name: Mark Pellow
Phone: 027 846 2093
email: markpellow@stockharbor.example
website: www.stockharbor.example

Font styles to use
Other font styles liked:
• Unsure

Colors
9bcb3b

Requirements
Must have
• coming soon
Nice to have
• coming soon
Should not have
• coming soon

```html
<!DOCTYPE html>
<html lang="en">
<head>
<meta charset="utf-8">
<title>StockHarbor Business Card</title>
<link rel="stylesheet" href="https://fonts.googleapis.com/css2?family=Raleway:wght@700;800&family=Lato:wght@400;700&display=swap">
<style>
  :root {
    --page-bg: #e9e9e7;
    --card-white: #ffffff;
    --card-mist: #f1f1f0;
    --charcoal: #333130;
    --brand-green: #9bcb3b;
    --text-light: #ffffff;
    --mascot-orange: #f3a52c;
    --mascot-green: #8cc43c;
  }
  * { box-sizing: border-box; margin: 0; padding: 0; }
  html, body { width: 1200px; height: 900px; overflow: hidden; }
  body { background: var(--page-bg); position: relative; font-family: "Lato", sans-serif; }

  .business-card {
    position: absolute; left: 111px; top: 148px;
    width: 978px; height: 603px;
    background: linear-gradient(180deg, var(--card-white) 0%, var(--card-mist) 100%);
    box-shadow: 0 10px 30px rgba(0,0,0,0.18);
    overflow: hidden;
  }
  .side-panel { position: absolute; left: 0; top: 0; width: 978px; height: 603px; }

  .brand-name {
    position: absolute; left: 440px; top: 78px;
    font-family: "Raleway", sans-serif; font-weight: 800;
    font-size: 66px; letter-spacing: -1px; line-height: 1;
    color: var(--charcoal);
  }

  .contact-block { position: absolute; left: 55px; top: 210px; color: var(--text-light); }
  .person-name {
    font-family: "Raleway", sans-serif; font-weight: 700;
    font-size: 41px; line-height: 1; margin-bottom: 42px;
  }
  .person-name .surname { color: var(--brand-green); }
  .contact-list { list-style: none; }
  .contact-list li {
    display: flex; align-items: center; gap: 8px;
    font-size: 26px; line-height: 37px;
  }
  .contact-list svg { width: 20px; height: 20px; fill: var(--brand-green); flex: none; }

  .service-list { list-style: none; margin-top: 38px; }
  .service-list li {
    display: flex; align-items: center; gap: 8px;
    font-size: 27px; line-height: 37px;
  }
  .service-list li::before {
    content: ""; width: 14px; height: 14px; border-radius: 50%;
    background: var(--text-light); flex: none;
  }

  .mascot-area {
    position: absolute; left: 603px; top: 220px; width: 330px; height: 353px;
    border-radius: 24px;
    background: radial-gradient(circle at 50% 45%, var(--mascot-orange) 0%, var(--mascot-green) 55%, rgba(140,196,60,0.25) 100%);
  }
</style>
</head>
<body>
  <article class="business-card">
    <svg class="side-panel" viewBox="0 0 978 603" aria-hidden="true">
      <path class="panel-edge" d="M0 0 H320 C330 200 620 230 640 360 C655 460 560 520 580 603 H0 Z"
            fill="var(--brand-green)" transform="translate(10 0)"/>
      <path class="panel-fill" d="M0 0 H320 C330 200 620 230 640 360 C655 460 560 520 580 603 H0 Z"
            fill="var(--charcoal)"/>
    </svg>

    <div class="brand-name">StockHarbor</div>

    <section class="contact-block">
      <h1 class="person-name">Mark <span class="surname">Pellow</span></h1>
      <ul class="contact-list">
        <li><svg viewBox="0 0 20 20"><path d="M3 7c0-2 3-4 7-4s7 2 7 4v2h-4V7H7v2H3zM5 10h10l2 7H3z"/></svg>027 846 2093</li>
        <li><svg viewBox="0 0 20 20"><path d="M2 4h16v12H2z M2 4l8 7 8-7" stroke="var(--charcoal)" stroke-width="1.5"/></svg>markpellow@stockharbor.example</li>
        <li><svg viewBox="0 0 20 20"><circle cx="10" cy="10" r="8"/><path d="M6 6c2 1 3 3 2 5M12 4c1 3 4 4 5 7M9 14c2 0 3 2 3 4" stroke="var(--charcoal)" stroke-width="1.4" fill="none"/></svg>www.stockharbor.example</li>
      </ul>
      <ul class="service-list">
        <li>Sell Excess Stock</li>
        <li>Manage Product Returns</li>
        <li>Sell Company Assets</li>
      </ul>
    </section>

    <div class="mascot-area" role="img" aria-label="Illustration of a running courier mascot carrying a parcel"></div>
  </article>
</body>
</html>
```